New webdesign for a cable company

We need a new design for Lumo Nett.

There exist a suggestion for the page, were we have attached files to show you this. The design here is not good enough, but here you can se what content we need.

You can feel free to give adjustment to this design to make it better, our blow us away with a new brilliant design, but from this design you see what content we need.

The important is that the company get a design who represent its products:
- TV = Cable TV
- Bredbånd = Broadband
- Mobil = Mobile phone
- Strøm = Electricity
- Alarm = Alarm
- Lumo Samlet = a cobain pagage of all our products.

Lumo Nett would like costumers who visit the site to het the impression that Lumo Nett is a professional, innovative and fun company.
Updates

We have to day uploaded pictures of the existing page as the link haven't been working for the most of you as it's placed on a server our developer are using and is often shut it down. 

We have also updated the brief with some new and updated description so please read true the updated brief. 

We will at the same time inform that we haven't been able to give feedback on any of the received design and are sorry for that, we will within the next 24 hours hopefully have started responded the different received designs.

Looking forward to see more suggestion and hope you will help us create and very professional and informative design. 

Reason: We have decided to extend the deadline due to the number of design suggestion who is sent in and your lack of response to all designers due to our own workload.

This project was unfortunately for different reason put on ice for a while, but we are now ready to complete the design and will answer and give feedback too all the received design suggestions. 

Within a couple of days we hope we have answered all you who sent us suggestions, we appreciate all suggestions and hope to get in more suggestions.

Reason: Deisgn description have been updated

Target Market(s)

Our costumer are both private and companies

Industry/Entity Type

Tv

Requirements
Must have
• A easy way to promote and inform about changes in our products, there are a constant change in our products and it must bee a easy and good way to changes ass the marked change. Cheek out this link, for a example of what we like/think of here, https://kabel.fjordvisjon.no

On all pages there must be a easy way to click on a order button and too inform about your interest (thats two different things), could be placed in the top right corner for example. In the order form you should follow a step by step part:
1. Cheek what product we can provide you.
2. Chooce products.
3. Costumer inforamtion.
4. Confirmation.

Somewere on the portal it must be possible for costumers to log on to their own administration, where they can cheek for invoices, other statuses, etc.

A main menu existing of:
Hjem (Home)
Produkter (Products)
Storkunde (key account/large costumers)
Kundeservice (Costumerservice)
Min side (My page)

The main menu should have the following sub titles:
- Under "Produkter"/products our different products must be listed
- Under "Kundeservice"/Costumerservice it must have these submenus:
- Hjelp og støtte = Help.
- Faktura = Invoice
- Brukerguider = Userguides
- Abbonementavtaler = Terms and conditions.

A bottom menu where we have 5 main categories, with sub categories:
Om oss (about us)
- Om Lumo Nett (about Lumo Nett)
- Kontaktinformajson ( contact information)
- Pressemeldinger (Pressrelese)
- Ledige stillinger (positions available)
- KRAB ( and organisastion in our field)

Produkter (Product)
- TV (TV)
- Bredbånd (Broadand)
- Telefoni (telephony, both mobil)
- Strøm (elecricity)
- Arlam (Alarm)

Borrettslag/Sameier (Housing cooperatives)
- Løsninger (solutions)
- Produkter (product)
- Kontaktpersoner (contactpersons)

Utbygger (developer)
- Hva vi kan gjøre for dere. (What we can do for you)

Opperatørnett (operators)

Build up the categories and bottom menu something like this:
https://kabel.fjordvisjon.no
www.brenvik.com
Nice to have
• A main menu existing of:
Hjem (Home)
Produkter (Products)
Lumo Nett
Kontakt oss (Contact us)

Under "Produkter"/products our different products must be listed and under "Kundeservice"/Costumerservice it must have these submenus:
- Hjelp og støtte = Help.
- Faktura = Invoice
Should not have
• Any translation section since the homepage only will be in Norwegian.

```html
<!DOCTYPE html>
<html lang="no">
<head>
<meta charset="utf-8">
<title>Lumo Nett – Mobile Phones</title>
<link href="https://fonts.googleapis.com/css2?family=Lato:ital,wght@0,300;0,400;0,700;0,900;1,300;1,400&display=swap" rel="stylesheet">
<style>
:root{
  --blue:#2ab4e4;
  --blue-dark:#1c9fd0;
  --green:#7cc242;
  --ink:#222426;
  --hero:#2a2d31;
  --panel:#ffffff;
  --page:#ebebeb;
  --bar:#45494d;
  --footer:#1c1d1f;
  --footer-text:#8c8f93;
  --text:#333;
}
*{margin:0;padding:0;box-sizing:border-box}
html,body{width:812px;height:1200px;overflow:hidden}
body{font-family:"Lato",sans-serif;color:var(--text);background:var(--page);position:relative}
.abs{position:absolute}

/* header */
.site-header{position:absolute;left:0;top:0;width:812px;height:69px;background:#fff}
.brand{position:absolute;left:136px;top:24px;display:flex;align-items:center;gap:8px;font-size:24px;font-weight:400;color:#3a3d41}
.brand .dot{width:22px;height:22px;border-radius:50%;background:var(--blue)}
.top-actions{position:absolute;left:452px;top:0;height:18px;display:flex}
.top-actions a{display:flex;align-items:center;gap:4px;font-size:9px;font-weight:900;color:#fff;text-decoration:none;padding:0 8px;text-transform:uppercase}
.top-actions .order{background:var(--green);padding-left:14px;clip-path:polygon(8px 0,100% 0,100% 100%,0 100%)}
.top-actions .interest{background:var(--blue)}
.top-actions i{width:9px;height:9px;border-radius:50%;background:#fff;display:inline-block}
.main-nav{position:absolute;left:346px;top:52px;display:flex;font-size:8.5px;font-weight:700;color:#333}
.main-nav a{color:inherit;text-decoration:none;padding:0 9px;border-left:1px solid #aaa;line-height:9px;height:9px}
.main-nav a:first-child{border-left:0}
.main-nav .active{position:relative}
.main-nav .active::after{content:"";position:absolute;left:-6px;right:-6px;top:14px;height:3px;background:var(--blue)}

/* hero */
.hero{position:absolute;left:0;top:69px;width:812px;height:193px;background:var(--hero)}
.hero-media{position:absolute;left:168px;top:11px;width:188px;height:148px;border-radius:6px;background:linear-gradient(90deg,#3a3c3f,#5a5d61 45%,#2d8fd0 60%,#e8e8e8)}
.hero h1{position:absolute;left:398px;top:21px;font-size:28px;font-weight:900;color:#fff;letter-spacing:-.5px}
.steps{position:absolute;left:398px;top:55px;list-style:none}
.steps li{font-size:14px;font-weight:300;color:#e8eaec;letter-spacing:-.6px;line-height:17.6px;display:flex;align-items:center;gap:4px}
.steps li svg{flex:none}
.btn-more{position:absolute;left:398px;top:134px;width:62px;height:17px;background:var(--blue);color:#fff;font-size:7px;font-weight:900;display:flex;align-items:center;justify-content:center}

/* content panel */
.panel{position:absolute;left:136px;top:238px;width:541px;height:654px;background:var(--panel);box-shadow:0 0 10px rgba(0,0,0,.12)}
.contact{position:absolute;left:15px;top:14px;font-size:12px;line-height:17.5px;color:#333}
.contact b{color:var(--blue);font-weight:400}
.rule{position:absolute;left:14px;right:14px;top:55px;height:1px;background:#e2e2e2}

.service{position:absolute;width:148px;height:111px;border:1px solid #ddd;background:linear-gradient(#fff,#f1f1f1)}
.service .icon{position:absolute;left:0;right:0;top:10px;display:flex;justify-content:center}
.service .price{position:absolute;left:0;right:0;top:73px;height:19px;background:var(--blue);color:#fff;font-size:10px;font-weight:900;padding-left:7px;display:flex;align-items:center}
.service .price span{font-weight:400;margin-left:4px;color:#111}
.service .more{position:absolute;left:0;right:0;top:92px;height:19px;background:var(--bar);color:#fff;font-size:9px;font-weight:400;padding:0 7px;display:flex;align-items:center;justify-content:space-between}
.service .more.dark{background:#000}
.more i{width:0;height:0;border-left:4px solid transparent;border-right:4px solid transparent;border-top:5px solid #fff}
.map{position:absolute;left:319px;top:66px;width:212px;height:229px;background:linear-gradient(135deg,#a8cdf2,#8fbbee 60%,#b9d6f4);border:1px solid #7fb0e6}

.products{position:absolute;left:14px;top:300px;width:518px;height:186px;border:1px solid #444}
.products h2{height:32px;background:#000;color:#fff;font-size:11px;font-weight:400;padding-left:11px;display:flex;align-items:center}
.product-row{position:absolute;left:0;right:0;display:flex}
.product{width:103.6px;display:flex;flex-direction:column;align-items:center;border-left:1px solid #eee}
.product:first-child{border-left:0}
.phone-img{width:52px;height:100px;border-radius:8px;background:linear-gradient(#2b2d30,#4b88c8 30%,#2e6fb0 70%,#222)}
.product .price{margin-top:9px;font-size:9.5px;color:var(--blue);letter-spacing:-.3px}
.product .check{margin-top:4px;width:8px;height:8px;border:1px solid #999}
.also{position:absolute;left:14px;top:504px;font-size:12px;font-weight:700;color:var(--blue)}
.arrow{position:absolute;top:536px}

/* search band */
.tab{position:absolute;left:284px;top:916px;width:268px;height:37px}
.tab-text{position:absolute;left:284px;top:924px;width:268px;text-align:center;font-size:17px;font-style:italic;font-weight:400;color:#fff;letter-spacing:-1.3px}
.band{position:absolute;left:0;top:952px;width:812px;height:56px;background:linear-gradient(#35bff0,var(--blue-dark))}
.field{position:absolute;top:8px;height:18px;background:#fff;border:1px solid #d3e9f3;display:flex;align-items:center;font-size:7px;color:#bbb}
.field .ic{width:22px;height:100%;display:flex;align-items:center;justify-content:center;border-right:1px solid #e4e4e4;margin-right:6px}
.find{position:absolute;left:618px;top:8px;width:60px;height:19px;background:#111;color:#fff;font-size:8px;font-weight:900;display:flex;align-items:center;justify-content:center;border:1px solid #fff}
.band p{position:absolute;left:0;right:0;top:33px;text-align:center;font-size:13px;font-style:italic;color:#fff;letter-spacing:-1px}

/* footer */
.site-footer{position:absolute;left:0;top:1008px;width:812px;height:192px;background:var(--footer)}
.fcol{position:absolute;top:20px}
.fcol h3{font-size:12px;font-weight:400;color:#fff;letter-spacing:-.6px;padding-bottom:2px;border-bottom:1px dotted #666;margin-bottom:4px}
.fcol li{list-style:none;font-size:9px;font-weight:300;color:var(--footer-text);line-height:14.6px;letter-spacing:-.4px}
.fcol .note{font-size:9px;font-weight:300;color:var(--footer-text);letter-spacing:-.5px;padding-bottom:6px;border-bottom:1px solid #3a3b3e;margin-bottom:4px}
.fbrand{position:absolute;left:548px;top:108px;width:130px;display:flex;align-items:center;justify-content:flex-end;gap:7px;font-size:20px;font-weight:400;color:#fff}
.fbrand .dot{width:18px;height:18px;border-radius:50%;background:#fff}
.terms{position:absolute;left:138px;top:134px;font-size:8px;font-weight:300;color:#777;letter-spacing:-.4px}
.fline{position:absolute;left:0;right:0;top:148px;height:1px;background:#333}
.copy{position:absolute;left:138px;top:158px;width:540px;font-size:8px;font-weight:300;color:#777;line-height:13px;letter-spacing:-.4px}
</style>
</head>
<body>

<header class="site-header">
  <div class="brand"><span class="dot"></span>Lumo Nett</div>
  <div class="top-actions">
    <a class="order" href="#"><i></i>Bli kunde i dag</a>
    <a class="interest" href="#"><i></i>Meld din interesse</a>
  </div>
  <nav class="main-nav">
    <a class="active" href="#">Hjem</a>
    <a href="#">Produkter</a>
    <a href="#">Storkunde</a>
    <a href="#">Kundeservice</a>
    <a href="#">Min Side</a>
    <a href="#">Kontakt Oss</a>
  </nav>
</header>

<section class="hero">
  <div class="hero-media" role="img" aria-label="Photo of a black smartphone with tiled home screen and a stylus"></div>
  <h1>MOBILE PHONES</h1>
  <ul class="steps">
    <li><svg width="16" height="10" viewBox="0 0 16 10"><path d="M1 5h3M6 5h3" stroke="#2ab4e4" stroke-width="2"/><path d="M11 1l4 4-4 4" fill="none" stroke="#2ab4e4" stroke-width="2"/></svg>Cheek What Product We Can Provide You.</li>
    <li><svg width="16" height="10" viewBox="0 0 16 10"><path d="M1 5h3M6 5h3" stroke="#2ab4e4" stroke-width="2"/><path d="M11 1l4 4-4 4" fill="none" stroke="#2ab4e4" stroke-width="2"/></svg>Chooce Products.</li>
    <li><svg width="16" height="10" viewBox="0 0 16 10"><path d="M1 5h3M6 5h3" stroke="#2ab4e4" stroke-width="2"/><path d="M11 1l4 4-4 4" fill="none" stroke="#2ab4e4" stroke-width="2"/></svg>Costumer Inforamtion.</li>
    <li><svg width="16" height="10" viewBox="0 0 16 10"><path d="M1 5h3M6 5h3" stroke="#2ab4e4" stroke-width="2"/><path d="M11 1l4 4-4 4" fill="none" stroke="#2ab4e4" stroke-width="2"/></svg>Confirmation.</li>
  </ul>
  <a class="btn-more">READ MORE</a>
</section>

<main class="panel">
  <div class="contact">
    <div><b>Addersse:</b> 47 Harbor Lane, Fairview, Oregon, United States</div>
    <div><b>Telefonnummer:</b> +1-555014827391</div>
  </div>
  <div class="rule"></div>

  <div class="service" style="left:14px;top:66px">
    <div class="icon"><svg width="64" height="56" viewBox="0 0 64 56"><path d="M24 8a24 24 0 1 1 4 45" fill="none" stroke="#222" stroke-width="4"/><path d="M40 8l-10 22h8l-6 18 14-24h-8l6-16z" fill="#222"/><rect x="6" y="24" width="14" height="14" rx="3" fill="#222"/><path d="M10 38v8M16 38v8M20 28h6M20 34h6" stroke="#222" stroke-width="3"/></svg></div>
    <div class="price">STARTING PRICE: <span>$ 250.00</span></div>
    <div class="more">More Information<i></i></div>
  </div>
  <div class="service" style="left:167px;top:66px">
    <div class="icon"><svg width="60" height="56" viewBox="0 0 60 56"><rect x="6" y="6" width="48" height="34" rx="5" fill="none" stroke="#222" stroke-width="5"/><path d="M26 40v8M34 40v8M18 50h24" stroke="#222" stroke-width="5"/></svg></div>
    <div class="price">STARTING PRICE: <span>$ 550.00</span></div>
    <div class="more">More Information<i></i></div>
  </div>
  <div class="service" style="left:14px;top:184px">
    <div class="icon"><svg width="64" height="56" viewBox="0 0 64 56"><rect x="20" y="16" width="36" height="26" rx="3" fill="none" stroke="#222" stroke-width="4"/><path d="M34 42v6M42 42v6M28 50h22" stroke="#222" stroke-width="4"/><path d="M6 28a20 20 0 0 1 20-20M12 28a14 14 0 0 1 14-14" fill="none" stroke="#222" stroke-width="3"/></svg></div>
    <div class="price">STARTING PRICE: <span>$ 350.00</span></div>
    <div class="more">More Information<i></i></div>
  </div>
  <div class="service" style="left:167px;top:184px">
    <div class="icon"><svg width="60" height="56" viewBox="0 0 60 56"><path d="M14 6c4-2 8 0 10 6l2 6c1 3-2 5-4 7 2 6 6 10 12 13 2-2 4-5 7-4l6 2c5 2 7 6 5 10-3 5-9 7-15 4C24 44 14 34 10 20 8 14 10 9 14 6z" fill="#222"/></svg></div>
    <div class="price">STARTING PRICE: <span>$ 425.00</span></div>
    <div class="more dark">More Information<i></i></div>
  </div>
  <div class="map" role="img" aria-label="World map showing the office location"></div>

  <section class="products">
    <h2>Telefoni Products</h2>
    <div class="product-row" style="top:46px">
      <div class="product"><div class="phone-img" role="img" aria-label="Smartphone photo"></div><div class="price">Price: $250</div><div class="check"></div></div>
      <div class="product"><div class="phone-img" role="img" aria-label="Smartphone photo"></div><div class="price">Price: $200</div><div class="check"></div></div>
      <div class="product"><div class="phone-img" role="img" aria-label="Keyboard phone photo"></div><div class="price">Price: $150</div><div class="check"></div></div>
      <div class="product"><div class="phone-img" role="img" aria-label="Smartphone photo"></div><div class="price">Price: $350</div><div class="check"></div></div>
      <div class="product"><div class="phone-img" role="img" aria-label="Smartphone photo"></div><div class="price">Price: $300</div><div class="check"></div></div>
    </div>
  </section>

  <div class="also">Customers Also Like Products:</div>
  <svg class="arrow" style="left:18px" width="10" height="16" viewBox="0 0 10 16"><path d="M8 1L2 8l6 7" fill="none" stroke="#999" stroke-width="1.2"/></svg>
  <svg class="arrow" style="left:518px" width="10" height="16" viewBox="0 0 10 16"><path d="M2 1l6 7-6 7" fill="none" stroke="#999" stroke-width="1.2"/></svg>
  <div class="product-row" style="left:15px;right:15px;top:530px">
    <div class="product"><div class="phone-img" role="img" aria-label="Smartphone photo"></div></div>
    <div class="product"><div class="phone-img" role="img" aria-label="Smartphone photo"></div></div>
    <div class="product"><div class="phone-img" role="img" aria-label="Keyboard phone photo"></div></div>
    <div class="product"><div class="phone-img" role="img" aria-label="Smartphone photo"></div></div>
    <div class="product"><div class="phone-img" role="img" aria-label="Smartphone photo"></div></div>
  </div>
</main>

<svg class="tab" viewBox="0 0 268 37" preserveAspectRatio="none"><path d="M0 37C20 37 22 0 46 0H222C246 0 248 37 268 37Z" fill="#35bff0"/></svg>
<div class="tab-text">Hvilke tjenester kan vi tilby deg</div>
<section class="band">
  <div class="field" style="left:138px;width:234px"><span class="ic"><svg width="10" height="8" viewBox="0 0 10 8"><rect width="10" height="8" rx="1" fill="#2ab4e4"/><path d="M0 1l5 4 5-4" fill="none" stroke="#fff"/></svg></span>Addresse</div>
  <div class="field" style="left:378px;width:234px"><span class="ic"><svg width="10" height="10" viewBox="0 0 10 10"><rect x="1" y="0" width="8" height="10" rx="1" fill="#2ab4e4"/></svg></span>Telefonnummer</div>
  <div class="find">FIND NOW</div>
  <p>Søk på adressen eller telefonummeret ditt for å se hvilke tjenester vi kan levere deg</p>
</section>

<footer class="site-footer">
  <div class="fcol" style="left:138px;width:58px"><h3>Om Oss</h3><ul><li>Om Lumo Nett</li><li>Kontaktinformajson</li><li>Pressemeldinger</li><li>Ledige stillinger</li><li>KRAB</li></ul></div>
  <div class="fcol" style="left:258px;width:74px"><h3>Produkter</h3><ul><li>TV</li><li>Bredbånd</li><li>Telefoni</li><li>Strøm</li><li>Arlam</li></ul></div>
  <div class="fcol" style="left:360px;width:130px"><h3>Borrettslag/Sameier</h3><ul><li>Løsninger</li><li>Produkter</li><li>Kontaktpersoner</li></ul></div>
  <div class="fcol" style="left:548px;width:130px">
    <h3>Utbygger</h3><div class="note">Hva vi kan gjøre for dere.</div>
    <h3 style="margin-top:6px">Opperatørnett</h3><div class="note" style="border:0">Hva vi kan gjøre for dere</div>
  </div>
  <div class="fbrand"><span class="dot"></span>Lumo Nett</div>
  <div class="terms">Ordinære vilkår Lumo Nett Kabel-TV Personinformasjon og cookies</div>
  <div class="fline"></div>
  <p class="copy">Lumo Nett Nordens største TV-distributør og Norges nest største bredbåndsleverandør. Vår virksomhet består av to enheter; Lumo Nett Kabel-TV AS og Lumo Nett Norge AS Copyright © 2013 Lumo Nett.</p>
</footer>

</body>
</html>
```